2020-23 Strategic Plan - Graphic Design Work

We would would like to have our strategic plan designed. It should be two pages.

- I am looking for suggestions on ways to lay this out. I don’t like this boxy layout. It was great for the committee as we went through multiple versions, but I’d prefer the final not follow this boxy format

- I’ve included a few images we own (feel free to use any or none of them). Also attached our logo.

- Have a look at our new website to see our new branding look and feel (launching next week) https://thevorlenta.example-hub.com/

- I've included a copy of our logo.

Target Market(s)

Membership

Other font styles liked:
• Lato

Requirements
Must have
• Excellent layout. Easy to ready. Consistent with branding.

```html
<!DOCTYPE html>
<html lang="en">
<head>
<meta charset="utf-8">
<title>VIA 2020-2023 Strategic Plan</title>
<link href="https://fonts.googleapis.com/css2?family=Montserrat:wght@400;500;600;700&display=swap" rel="stylesheet">
<style>
:root{
  --backdrop:#e0dede;
  --green:#4c9234;
  --dark-green:#1f4a25;
  --white:#ffffff;
  --ink:#2a2a2a;
  --photo-a:#b9c8d6;
  --photo-b:#6f8296;
  --photo-c:#c8b6a3;
  --photo-d:#8a7a6a;
}
*{box-sizing:border-box;margin:0;padding:0}
html,body{width:1200px;height:1180px;overflow:hidden;background:var(--backdrop);font-family:"Montserrat",sans-serif}
.page{position:absolute;left:312px;width:576px;height:324px;overflow:hidden}
.page-front{top:256px;background:var(--white)}
.page-back{top:600px;background:var(--green)}
.intro{position:absolute;left:31px;top:35px;width:130px;color:var(--ink)}
.brand{display:flex;align-items:center;gap:5px;color:var(--dark-green);font-weight:700;font-size:15px;letter-spacing:.5px}
.brand-dot{width:12px;height:12px;border-radius:50%;background:var(--green)}
.brand-sub{font-size:4.2px;font-weight:700;color:var(--dark-green);margin-top:2px;letter-spacing:.2px}
.plan-title{margin-top:20px;font-size:11px;font-weight:700;color:var(--dark-green);line-height:1.3}
.intro-text{margin-top:10px;font-size:6.4px;line-height:1.22;font-weight:500}
.date{margin-top:14px;font-size:8.5px;font-weight:700;color:var(--green)}
.site{margin-top:2px;font-size:5.6px;font-weight:700;color:var(--ink)}
.photo-group{position:absolute;left:180px;top:0;width:396px;height:162px;background:linear-gradient(100deg,var(--photo-a),var(--photo-b) 55%,var(--photo-a) 80%,#d8dee3)}
.values-band{position:absolute;left:180px;top:162px;width:396px;height:162px;background:var(--green)}
.pillar{position:absolute;color:var(--white)}
.icon-ring{width:41px;height:41px;border:1.2px solid var(--white);border-radius:50%;display:flex;align-items:center;justify-content:center}
.icon-ring svg{width:18px;height:18px;stroke:var(--white);fill:none;stroke-width:1.6;stroke-linecap:round;stroke-linejoin:round}
.pillar-title{font-size:8.5px;font-weight:500;margin-top:8px}
.pillar-text{font-size:4.9px;line-height:1.22;font-weight:500;margin-top:5px;width:86px}
.values-band .pillar{top:19px}
.goal{position:absolute;top:19px;width:92px;color:var(--white)}
.goal-title{font-size:8.5px;font-weight:700;margin-top:7px}
.goal-label{font-size:5px;font-weight:700;margin-top:8px}
.goal-text{font-size:4.9px;line-height:1.22;font-weight:500;margin-top:4px}
.goal-text+.goal-text{margin-top:6px}
.goal ul{list-style:none;margin-top:4px}
.goal li{font-size:4.9px;line-height:1.22;font-weight:500;padding-left:4px;position:relative;margin-bottom:3px}
.goal li::before{content:"•";position:absolute;left:0}
.photo-study{position:absolute;left:438px;top:0;width:138px;height:324px;background:linear-gradient(160deg,var(--photo-d),var(--photo-c) 45%,#ece6df)}
.brand-reverse{position:absolute;left:473px;top:279px;color:var(--white)}
.brand-reverse .brand{color:var(--white);font-size:13px}
.brand-reverse .brand-dot{background:var(--white)}
.brand-reverse .brand-sub{color:var(--white)}
</style>
</head>
<body>
<section class="page page-front">
  <div class="intro">
    <div class="brand"><span class="brand-dot"></span>VIA</div>
    <div class="brand-sub">VORLENTA INSTITUTE OF ASSESSORS</div>
    <h1 class="plan-title">2020-2023<br>STRAGETIC PLAN</h1>
    <p class="intro-text">With over 1,250 members, the Vorlenta Institute of Assessors is Canada's largest association of property assessment and taxation professionals. Our diverse membership is comprised of individuals from the private and public sectors practicing in the fields of assessment, consultancy, appraisal, taxation and law. Incorporated in May 1957, the VIA is dedicated to advancing the interests, education and professional competence of its members. Our members are highly qualified and widely recognized as the leading professionals in the property assessment industry.</p>
    <p class="date">JULY 2020</p>
    <p class="site">www.thevorlenta.example-hub.com</p>
  </div>
  <div class="photo-group" role="img" aria-label="Photo of a group of people seated in a discussion circle"></div>
  <div class="values-band">
    <div class="pillar" style="left:34px">
      <div class="icon-ring"><svg viewBox="0 0 24 24"><circle cx="7" cy="15" r="4"/><circle cx="17" cy="15" r="4"/><path d="M9 11l1-5h4l1 5M10 14h4"/></svg></div>
      <h2 class="pillar-title">Vision</h2>
      <p class="pillar-text">To be the industry leader in education, ethical standards, and professional accreditation in the field of property assessment in Canada.</p>
    </div>
    <div class="pillar" style="left:155px">
      <div class="icon-ring"><svg viewBox="0 0 24 24"><path d="M5 21L12 8M19 21L12 8M5 8l4-3 3 3M19 8l-4-3-3 3"/></svg></div>
      <h2 class="pillar-title">Mision</h2>
      <p class="pillar-text">To provide specialized education through a comprehensive approach to training which embraces all available technologies. To promote professional development and to ensure our members are recognized as experts in the field of property assessment and related functions.</p>
    </div>
    <div class="pillar" style="left:276px">
      <div class="icon-ring"><svg viewBox="0 0 24 24"><circle cx="12" cy="9" r="5"/><path d="M9 13l-2 7 3-1 2 2M15 13l2 7-3-1-2 2"/></svg></div>
      <h2 class="pillar-title">Values</h2>
      <p class="pillar-text">The Vorlenta Institute of Assessors and its members value professionalism, inclusivity, diversity, integrity, ethics, accountability, and expertise. The VIA is committed to serving all members and stakeholders with competence and respect, rejecting all forms of prejudice and discrimination.</p>
    </div>
  </div>
</section>

<section class="page page-back">
  <div class="goal" style="left:22px">
    <div class="icon-ring"><svg viewBox="0 0 24 24"><path d="M3 6h7a2 2 0 0 1 2 2v11a2 2 0 0 0-2-2H3zM21 6h-7a2 2 0 0 0-2 2v11a2 2 0 0 1 2-2h7z"/></svg></div>
    <h2 class="goal-title">Educate</h2>
    <p class="goal-label">Strategic Objective</p>
    <p class="goal-text">Be the most trusted, relevant, and accessible provider of education and credentials in the field of property assessment in Canada</p>
    <p class="goal-label">Strategic Goals</p>
    <p class="goal-text">Ensure a catalogue of relevant, high-quality courses, which meet the evolving needs of assessment professionals</p>
    <p class="goal-text">Provide an equal VIA member experience and service, regardless of geography</p>
    <p class="goal-label">Sample Supporting Actions</p>
    <ul>
      <li>Utilize technology to offer interactive and accessible online events</li>
      <li>Develop provincial legislation-specific content for VIA courses</li>
      <li>Lead opportunities for collaboration across districts to increase access to quality PD opportunities</li>
    </ul>
  </div>
  <div class="goal" style="left:125px">
    <div class="icon-ring"><svg viewBox="0 0 24 24"><path d="M3 17l6-6 4 4 8-8M15 7h6v6"/></svg></div>
    <h2 class="goal-title">Grow</h2>
    <p class="goal-label">Strategic Objective</p>
    <p class="goal-text">Increase the VIA's membership by serving all career levels and forging strong strategic partnerships.</p>
    <p class="goal-label">Strategic Goals</p>
    <p class="goal-text">Enhance opportunities for senior assessment professionals through the FVIA designation.</p>
    <p class="goal-text">Connect with young professionals by enhancing member communications, improving member onboarding, and expanding scholarship opportunities.</p>
    <p class="goal-label">Sample Supporting Actions</p>
    <ul>
      <li>Develop framework for a specialist designation track</li>
      <li>Work collaboratively with strategic partners from across the country to develop criteria for, and launch, the FVIA designation</li>
      <li>Redesign the new member onboarding experience</li>
    </ul>
  </div>
  <div class="goal" style="left:231px">
    <div class="icon-ring"><svg viewBox="0 0 24 24"><path d="M7 21V4M7 4h10v8H7"/></svg></div>
    <h2 class="goal-title">Lead</h2>
    <p class="goal-label">Strategic Objective</p>
    <p class="goal-text">Strengthen the reputation of the organization and its members by acting as a leader within the field of property assessment in Canada</p>
    <p class="goal-label">Strategic Goals</p>
    <p class="goal-text">Embrace the role of leader and advocate within the property assessment profession</p>
    <p class="goal-text">Strengthen current, and develop new, strategic partnerships with peer associations across Canada.</p>
    <p class="goal-label">Sample Supporting Actions</p>
    <ul>
      <li>Adopt an advocacy voice for the assessment profession to ensure interests are being represented</li>
      <li>Work with strategic partners to produce industry white papers with national relevance</li>
      <li>Engage with various levels of government across Canada</li>
    </ul>
  </div>
  <div class="goal" style="left:336px">
    <div class="icon-ring"><svg viewBox="0 0 24 24"><circle cx="12" cy="12" r="8"/><path d="M12 4v16M8 9h4M12 15h4"/></svg></div>
    <h2 class="goal-title">Govern</h2>
    <p class="goal-label">Strategic Objective</p>
    <p class="goal-text">Fortify the future of the VIA through operational excellence and a diverse group of talented volunteers</p>
    <p class="goal-label">Strategic Goals</p>
    <p class="goal-text">Review and align association management practices with strategic objectives and statements of Vision, Mission and Values.</p>
    <p class="goal-text">Secure the VIA's financial stability by reviewing current pricing model and practicing sound risk management.</p>
    <p class="goal-label">Sample Supporting Actions</p>
    <ul>
      <li>Align the VIA budget and staffing needs to achieve clear strategic objectives</li>
      <li>Utilize automation to modernize systems and administrative processes</li>
      <li>Review and assess the relevance of current committees to determine if sufficient to meet the requirements of the strategic plan, and create new committees if deemed relevant</li>
    </ul>
  </div>
  <div class="photo-study" role="img" aria-label="Photo of a young woman with a headset studying at a desk"></div>
  <div class="brand-reverse">
    <div class="brand"><span class="brand-dot"></span>VIA</div>
    <div class="brand-sub">VORLENTA INSTITUTE OF ASSESSORS</div>
  </div>
</section>
</body>
</html>
```